Web Design Project

This as the foundation http://lunorbix.com/demo_viewer/index.php?theme=velquistwp

Site needs to have a glossy black background with white text…..Extremely modern with a few flares of ravelle 6 style but nothing too off the wall, easily understood.

Here are some other reference sites and likes and dislikes that will help: (Probably overkill but we are looking for a cutting edge New York / LA Style )

http://www.torvikandcolb.com

Like- The black background with white font is very eye catching and clean. Love the contrast. Black is a great background for photographs and videos

http://samuelvorne.com

Like- Clean homepage, black and white color scheme works well.

http://douglaswhitcanephotography.com

Like- Nice Menu, nice B and W contrast

http://www.qkv.com

Like- Like the Menu. Clean and easy.

http://www.saffelmont.com

Like- Contrast of white background with black font.

Like- Slide show of stills (but should be able to click images to go to video. We’d also like the name of the project)

Like- Drop down menu allows for customer to find service they need without going through all services.

Like- Tells you work that they do right next to the logo.

Dislike- Too much information on homepage. Too much scrolling.

http://www.corbelvanestudios.com

Like- High Res images on home page

Like - The About Me is on homepage and speaks to potential customer directly. “We create award-winning videos for companies like yours.”

Like- Blog is updated with new projects they do. And short, visual entries

Like- “Work” section stands out from website. The background fades to light grey and white when you click on “work” so that the portfolio stands out more. Makes color look more vivid

Like- Black and white color scheme with grey header

http://www.fennwick748.com

Like- High Res images on home page pointing to projects

Like- Photograph as background, changes with different links. So work is always showcased and creates contrast. Information is laid over a barely translucent background, which is laid over the picture.

Like- They have a good Attitude about quality of their product

http://www.quillbramt.net

Like- First thing you see when open page is a clear big statement about what they do, said in a catchy way. They have a Tagline.

http://plimsworthdesign.com

Like- How work is categorized. Client list has links, which take you to their Client page with all their work grouped together. Nice flow and organization shows client relationships. And nice descriptions of what the job was and how it was executed… Way too wordy at times though

http://www.marivantphotography.com

Like- The homepage is very clean and accessible. Love the color scheme and how Logo is centered between the links.

Of the four designs we have gotten EVERY SINGLE ONE has been a template STOLEN from another site. We are paying for ORIGINAL design. Not copies and templates. Please ONLY submit original designs

```html
<!DOCTYPE html>
<html lang="en">
<head>
<meta charset="utf-8">
<title>Video Productions</title>
<link rel="stylesheet" href="https://fonts.googleapis.com/css2?family=Open+Sans:wght@300;400;600&display=swap">
<style>
  :root {
    --ink-dark: #222222;
    --nav-dark: #151515;
    --menu-dark: #1c1c1c;
    --accent: #1fc8bd;
    --paper: #ffffff;
    --text-light: #f2f2f2;
    --text-muted: #cfcfcf;
    --text-dark: #222222;
    --ring: #d9d9d9;
    --arrow: #3a3a3a;
    --hero-violet: #6a4fb8;
    --hero-shade: #2e2e3a;
    --social-grey: #4a4a4a;
  }
  * { margin: 0; padding: 0; box-sizing: border-box; }
  html, body { width: 1200px; height: 1054px; overflow: hidden; }
  body {
    position: relative;
    background: var(--paper);
    font-family: "Open Sans", "Segoe UI", sans-serif;
    color: var(--text-dark);
  }
  .site-header {
    position: absolute; left: 0; top: 0; width: 1200px; height: 150px;
    background: var(--ink-dark);
  }
  .brand {
    position: absolute; left: 177px; top: 32px;
    font-size: 30px; font-weight: 300; color: var(--accent); letter-spacing: 0.3px;
  }
  .search-icon { position: absolute; left: 990px; top: 32px; }
  .main-nav {
    position: absolute; left: 174px; top: 101px; width: 854px; height: 49px;
    background: var(--nav-dark);
  }
  .main-nav a {
    position: absolute; top: 0; height: 49px; line-height: 49px;
    font-size: 12px; color: var(--text-light); text-decoration: none;
    transform: translateX(-50%);
  }
  .main-nav .is-active::before {
    content: ""; position: absolute; left: 50%; top: 0; width: 86px; height: 2px;
    margin-left: -43px; background: var(--accent);
  }
  .dropdown {
    position: absolute; left: 172px; top: 150px; width: 163px; height: 132px;
    background: var(--menu-dark); list-style: none; z-index: 3;
  }
  .dropdown li {
    position: absolute; left: 18px; font-size: 12px; color: var(--text-light);
  }
  .dropdown .is-current { left: 25px; color: var(--accent); }
  .hero { position: absolute; left: 0; top: 150px; width: 1200px; height: 407px; background: var(--paper); }
  .hero-image {
    position: absolute; left: 154px; top: 24px; width: 357px; height: 357px; border-radius: 50%;
    background: linear-gradient(160deg, var(--hero-violet), var(--hero-shade));
  }
  .hero-title {
    position: absolute; left: 505px; width: 600px; top: 293px;
    text-align: center; font-size: 44px; font-weight: 300; color: #1e1e1e; letter-spacing: 0.3px;
    white-space: nowrap;
  }
  .hero-sub {
    position: absolute; left: 519px; width: 600px; top: 353px;
    text-align: center; font-size: 15.5px; font-weight: 300; color: #2a2a2a;
    white-space: nowrap;
  }
  .slide-arrow { position: absolute; top: 337px; }
  .slide-arrow.prev { left: 28px; }
  .slide-arrow.next { left: 1142px; }
  .intro-band {
    position: absolute; left: 0; top: 557px; width: 1200px; height: 97px;
    background: var(--ink-dark); color: var(--text-light);
    text-align: center; font-size: 19px; font-weight: 300; line-height: 97px;
  }
  .intro-band em { font-style: normal; color: var(--accent); }
  .feature {
    position: absolute; top: 716px; width: 160px; text-align: center;
    transform: translateX(-50%);
  }
  .feature-ring {
    display: block; margin: 0 auto; width: 108px; height: 108px; border-radius: 50%;
    border: 1px solid var(--ring);
  }
  .feature-label { display: block; margin-top: 13px; font-size: 12px; font-weight: 600; color: #222; }
  .site-footer {
    position: absolute; left: 0; top: 924px; width: 1200px; height: 130px;
    background: var(--ink-dark); color: var(--text-light);
  }
  .social { position: absolute; top: 43px; left: 492px; display: flex; gap: 16px; }
  .social span { width: 40px; height: 40px; border-radius: 50%; background: var(--social-grey); display: block; }
  .copyright {
    position: absolute; top: 108px; left: 0; width: 1200px; text-align: center;
    font-size: 11.5px; font-weight: 600;
  }
  .contact {
    position: absolute; left: 850px; top: 40px; font-size: 12px; font-weight: 300;
    color: var(--text-muted); line-height: 15px;
  }
  .contact p + p { margin-top: 15px; }
</style>
</head>
<body>
  <header class="site-header">
    <div class="brand">Your Logo</div>
    <svg class="search-icon" width="24" height="24" viewBox="0 0 24 24" aria-label="Search">
      <circle cx="8" cy="8" r="5" fill="none" stroke="#fff" stroke-width="2.4"/>
      <line x1="12" y1="12" x2="19" y2="18" stroke="#fff" stroke-width="3.4" stroke-linecap="round"/>
    </svg>
    <nav class="main-nav">
      <a class="is-active" style="left:43px">Home</a>
      <a style="left:132px">Service</a>
      <a style="left:219px">Gallery</a>
      <a style="left:309px">About</a>
      <a style="left:397px">Contact</a>
      <a style="left:485px">Blog</a>
    </nav>
  </header>

  <ul class="dropdown">
    <li style="top:15px">Show Reels</li>
    <li class="is-current" style="top:42px">Actor Demo Reels</li>
    <li style="top:71px">Client List</li>
    <li style="top:99px">Client Testimonials</li>
  </ul>

  <section class="hero">
    <div class="hero-image" role="img" aria-label="Slide photograph: close-up of a camera lens"></div>
  </section>
  <h1 class="hero-title">Endless Possibiliteis</h1>
  <p class="hero-sub">Bringing you the Best of Video Production With Award Winning Editors</p>
  <svg class="slide-arrow prev" width="32" height="48" viewBox="0 0 32 48" aria-label="Previous slide">
    <polyline points="27,3 6,24 27,45" fill="none" stroke="var(--arrow)" stroke-width="5"/>
  </svg>
  <svg class="slide-arrow next" width="32" height="48" viewBox="0 0 32 48" aria-label="Next slide">
    <polyline points="5,3 26,24 5,45" fill="none" stroke="var(--arrow)" stroke-width="5"/>
  </svg>

  <section class="intro-band">HD Video Production: <em>High definition</em> video, location, and studio shoots, post production with award winning editors.</section>

  <div class="feature" style="left:302px">
    <svg class="feature-ring" viewBox="0 0 108 108" aria-label="Idea">
      <path d="M48 47a7 7 0 1 1 12 5l-1 4h-10l-1-4a7 7 0 0 1 0-5z" fill="none" stroke="#333" stroke-width="1.4"/>
      <line x1="50" y1="59" x2="58" y2="59" stroke="#333" stroke-width="1.4"/>
      <line x1="51" y1="62" x2="57" y2="62" stroke="#333" stroke-width="1.4"/>
      <g stroke="#333" stroke-width="1.2"><line x1="54" y1="36" x2="54" y2="39"/><line x1="42" y1="44" x2="45" y2="45"/><line x1="66" y1="44" x2="63" y2="45"/><line x1="41" y1="51" x2="44" y2="51"/><line x1="67" y1="51" x2="64" y2="51"/></g>
    </svg>
    <span class="feature-label">Great Ideas</span>
  </div>
  <div class="feature" style="left:601px">
    <svg class="feature-ring" viewBox="0 0 108 108" aria-label="Price">
      <circle cx="54" cy="54" r="11" fill="none" stroke="#333" stroke-width="1.6"/>
      <text x="54" y="59" text-anchor="middle" font-size="13" font-family="Open Sans, sans-serif" fill="#333">$</text>
    </svg>
    <span class="feature-label">Affordable Price</span>
  </div>
  <div class="feature" style="left:899px">
    <svg class="feature-ring" viewBox="0 0 108 108" aria-label="Quality">
      <path d="M46 56l12-12h7v7l-12 12z" fill="none" stroke="#333" stroke-width="1.6" stroke-linejoin="round"/>
      <line x1="46" y1="56" x2="42" y2="64" stroke="#333" stroke-width="1.6"/>
    </svg>
    <span class="feature-label">High Quality Output</span>
  </div>

  <footer class="site-footer">
    <div class="social" aria-label="Social links">
      <span role="img" aria-label="Social link"></span>
      <span role="img" aria-label="Social link"></span>
      <span role="img" aria-label="Social link"></span>
      <span role="img" aria-label="Social link"></span>
    </div>
    <p class="copyright">Copyright 2013 | Privacy Policy</p>
    <div class="contact">
      <p>Video Productions</p>
      <p>48 W.17th Street, Suite 310<br>New York, NY 10011 212-555-0148</p>
    </div>
  </footer>
</body>
</html>
```